Business cards for education company

We need a business card design for a relatively new company based in Queensland and operating across Australia. We resell diploma level education courses which include Business, Management, Finance, Community Services & Government courses. We offer over 20 different courses.
The target market is for anyone 16 years of age and older. There is no age limit.

We would like to see the design use the color blue and silver. The final design should communicate professionalism and a bright future.

We sell education but are also promoting the career they see themselves in 2-3 years in the future

Our company logo is attached.

Target Market(s)

We target all age groups above 16 years of age. The main target market would be people aged between 17-35.

We focus on those people who cannot make it into University or do not want to commit the time to a full degree.

Industry/Entity Type

Education

Requirements
Must have
• Professional
Company logo
website
Contact details:

Please use the following example:

Lionel Parfitt
Senior Education Consultant
0417 386 591
Lionel.parfitt@brightwaylearninghub.com.au
www.brightwaylearninghub.com.au

```html
<!DOCTYPE html>
<html lang="en">
<head>
<meta charset="utf-8">
<title>Brightway Learning Hub – Business Card</title>
<link rel="stylesheet" href="https://fonts.googleapis.com/css2?family=Open+Sans:wght@400;600;700&display=swap">
<style>
  :root {
    --backdrop: #e9e7e4;
    --card: #ffffff;
    --ink: #1d1d1f;
    --brand-navy: #1b2f86;
    --brand-blue: #3b8fe0;
    --brand-deep: #101c5e;
    --silver: #5d6066;
    --white: #ffffff;
  }
  * { box-sizing: border-box; margin: 0; padding: 0; }
  html, body {
    width: 1200px; height: 443px; overflow: hidden;
    background: var(--backdrop);
    font-family: "Open Sans", Arial, sans-serif;
    color: var(--ink);
  }
  .sheet {
    position: relative; width: 1200px; height: 443px;
    display: flex; justify-content: center; align-items: center; gap: 40px;
  }
  .card {
    position: relative; width: 540px; height: 310px;
    background: var(--card);
    box-shadow: 0 6px 18px rgba(0,0,0,.18);
    overflow: hidden;
  }

  /* Front */
  .brand {
    position: absolute; top: 44px; left: 0; right: 0;
    display: flex; justify-content: center; align-items: center; gap: 12px;
  }
  .brand__dot {
    width: 38px; height: 38px; border-radius: 50%;
    background: var(--brand-blue);
  }
  .brand__name {
    font-weight: 700; font-size: 24px; letter-spacing: .5px;
    color: var(--brand-navy); text-transform: uppercase;
  }
  .contact {
    position: absolute; top: 132px; left: 0; right: 0;
    list-style: none; display: flex; flex-direction: column; align-items: center; gap: 5px;
    padding-left: 80px;
  }
  .contact__item {
    display: flex; align-items: center; gap: 6px;
    font-size: 12.5px; color: var(--ink);
  }
  .contact__icon { width: 12px; height: 12px; flex: none; }
  .swoosh { position: absolute; left: 0; bottom: 0; width: 540px; height: 120px; }
  .holder {
    position: absolute; left: 96px; bottom: 18px; color: var(--white);
  }
  .holder__name { font-weight: 700; font-size: 20px; line-height: 1.1; }
  .holder__title { font-size: 12.5px; }

  /* Back */
  .back__brand {
    position: absolute; top: 0; left: 0; right: 0; bottom: 60px;
    display: flex; flex-direction: column; justify-content: center; align-items: center; gap: 18px;
  }
  .back__dot {
    width: 110px; height: 110px; border-radius: 50%;
    background: var(--brand-blue);
  }
  .back__name {
    font-weight: 700; font-size: 30px; letter-spacing: .5px;
    color: var(--brand-navy); text-transform: uppercase;
  }
  .back__web {
    position: absolute; left: 0; right: 0; bottom: 40px;
    display: flex; justify-content: center; align-items: center; gap: 6px;
    font-weight: 600; font-size: 13px; color: var(--ink);
  }
</style>
</head>
<body>
<main class="sheet">

  <section class="card card--front" aria-label="Card front">
    <div class="brand">
      <span class="brand__dot"></span>
      <span class="brand__name">Brightway Learning Hub</span>
    </div>

    <ul class="contact">
      <li class="contact__item">
        <svg class="contact__icon" viewBox="0 0 12 12"><circle cx="6" cy="6" r="5.5" fill="none" stroke="#1d1d1f"/><path d="M4 3.2 L5 3 L5.6 4.6 L4.9 5.1 Q5.6 6.6 6.9 7.2 L7.4 6.5 L9 7.1 L8.8 8.1 Q5 8.6 3.8 4.2Z" fill="#1d1d1f"/></svg>
        0417 386 591
      </li>
      <li class="contact__item">
        <svg class="contact__icon" viewBox="0 0 12 12"><rect x="1" y="3" width="10" height="7" rx="1" fill="#1d1d1f"/><path d="M1.5 3.5 L6 7 L10.5 3.5" fill="none" stroke="#fff" stroke-width="1"/></svg>
        Lionel.parfitt@brightwaylearninghub.com.au
      </li>
      <li class="contact__item">
        <svg class="contact__icon" viewBox="0 0 12 12"><circle cx="6" cy="6" r="5.5" fill="#1d1d1f"/><path d="M0.5 6 H11.5 M6 0.5 V11.5 M6 0.5 Q2.5 6 6 11.5 M6 0.5 Q9.5 6 6 11.5" fill="none" stroke="#fff" stroke-width=".8"/></svg>
        www.brightwaylearninghub.com.au
      </li>
    </ul>

    <svg class="swoosh" viewBox="0 0 540 120" preserveAspectRatio="none" aria-hidden="true">
      <defs>
        <linearGradient id="bandGradient" x1="0" y1="0" x2="1" y2="0">
          <stop offset="0" stop-color="#4b9de8"/>
          <stop offset=".55" stop-color="#2a56c0"/>
          <stop offset="1" stop-color="#101c5e"/>
        </linearGradient>
      </defs>
      <path d="M0 56 Q260 42 540 6" fill="none" stroke="#5d6066" stroke-width="7"/>
      <path d="M0 68 Q260 52 540 14 L540 120 L0 120 Z" fill="url(#bandGradient)"/>
    </svg>

    <div class="holder">
      <p class="holder__name">Lionel Parfitt</p>
      <p class="holder__title">Senior Education Consultant</p>
    </div>
  </section>

  <section class="card card--back" aria-label="Card back">
    <div class="back__brand">
      <span class="back__dot"></span>
      <span class="back__name">Brightway Learning Hub</span>
    </div>
    <p class="back__web">
      <svg class="contact__icon" viewBox="0 0 12 12"><circle cx="6" cy="6" r="5.5" fill="#1b2f86"/><path d="M0.5 6 H11.5 M6 0.5 V11.5 M6 0.5 Q2.5 6 6 11.5 M6 0.5 Q9.5 6 6 11.5" fill="none" stroke="#fff" stroke-width=".8"/></svg>
      www.brightwaylearninghub.com.au
    </p>
  </section>

</main>
</body>
</html>
```